Design a premium label for the most expensive honey in the world: Manuka honey.

Manuka honey is originaire from New Zealand and recognized for its natural antibacterial activity. Rare and expensive, it is used in hospital as medical grade mainly to cure burns and wounds... Household will use it out of a pot like a "supplement" or to cure all sorts of ailments.
The label must feel:
- Premium and elegant .
- Reflect strongly its origin New Zealand. Use maori design but be careful of copyright. Must be styled.
- Purity and trust it is the real deal. Feel strongly that it is not an ersatz...
- Health and "medical" use.
Label must have:
* Brand: TOROWAI DOWNS
* MANUKA HONEY
* Made in New Zealand
* e250g
* MGO300
Target Market(s)
Export.

```html
<!DOCTYPE html>
<html lang="en">
<head>
<meta charset="utf-8">
<title>Torowai Downs Manuka Honey Label</title>
<link rel="stylesheet" href="https://fonts.googleapis.com/css2?family=Cinzel:wght@600;700&family=Exo+2:wght@600&family=Oswald:wght@300&display=swap">
<style>
  :root {
    --forest: #1f5a1c;
    --forest-deep: #0f3a0c;
    --gold: #f0c462;
    --gold-soft: #f5d48a;
    --cream: #f4f0e6;
    --ink: #3a3532;
    --page: #ffffff;
  }
  html, body {
    margin: 0;
    padding: 0;
    width: 1200px;
    height: 588px;
    overflow: hidden;
    background: var(--page);
  }
  .label-canvas {
    width: 1200px;
    height: 588px;
    display: block;
  }
  .label-outline { fill: var(--cream); stroke: var(--forest); stroke-width: 3; }
  .label-trim { fill: none; stroke: var(--gold); stroke-width: 3; }
  .origin-line {
    font-family: "Exo 2", sans-serif;
    font-weight: 600;
    font-size: 36px;
    fill: var(--forest);
    letter-spacing: 1px;
  }
  .dotted-rule { stroke: var(--ink); stroke-width: 2.4; stroke-dasharray: 0.1 7.2; stroke-linecap: round; }
  .grade-badge { fill: var(--forest-deep); stroke: var(--gold); stroke-width: 2; }
  .grade-text {
    font-family: "Cinzel", serif;
    font-weight: 700;
    font-size: 30px;
    fill: var(--gold);
  }
  .brand-name {
    font-family: "Cinzel", serif;
    font-weight: 700;
    font-size: 74px;
    fill: var(--gold);
  }
  .brand-name-shadow { fill: var(--forest); }
  .pattern-band { fill: var(--gold-soft); }
  .band-rule { stroke: var(--gold); stroke-width: 2; }
  .product-badge { fill: var(--forest-deep); }
  .product-flourish { fill: none; stroke: var(--gold); stroke-width: 1.6; }
  .product-text {
    font-family: "Cinzel", serif;
    font-weight: 700;
    font-size: 31px;
    fill: var(--gold);
  }
  .net-weight {
    font-family: "Oswald", sans-serif;
    font-weight: 300;
    font-size: 42px;
    fill: var(--ink);
  }
</style>
</head>
<body>
<svg class="label-canvas" viewBox="0 0 1200 588" xmlns="http://www.w3.org/2000/svg">
  <defs>
    <path id="origin-arc" d="M 370 218 Q 600 136 828 218"/>
  </defs>

  <!-- Label body -->
  <path class="label-outline" d="M 147 205 L 290 205 Q 330 150 440 125 Q 520 108 599 107 Q 680 108 760 125 Q 868 150 907 205 L 1052 205 Q 1079 205 1079 232 L 1079 483 Q 1079 510 1052 510 L 147 510 Q 120 510 120 483 L 120 232 Q 120 205 147 205 Z"/>
  <path class="label-trim" d="M 149 211 L 293 211 Q 333 157 442 131 Q 521 114 599 113 Q 679 114 758 131 Q 865 157 904 211 L 1050 211 Q 1073 211 1073 234 L 1073 481 Q 1073 504 1050 504 L 149 504 Q 126 504 126 481 L 126 234 Q 126 211 149 211 Z"/>

  <!-- Origin -->
  <text class="origin-line"><textPath href="#origin-arc" startOffset="50%" text-anchor="middle" textLength="450" lengthAdjust="spacing">MADE IN NEW ZEALAND</textPath></text>

  <!-- Dotted rule -->
  <line class="dotted-rule" x1="134" y1="265" x2="468" y2="265"/>
  <line class="dotted-rule" x1="704" y1="265" x2="1066" y2="265"/>

  <!-- Grade badge -->
  <path class="grade-badge" d="M 478 236 Q 585 242 692 236 Q 699 236 699 243 Q 696 265 699 287 Q 699 294 692 294 Q 585 290 478 294 Q 471 294 471 287 Q 474 265 471 243 Q 471 236 478 236 Z"/>
  <text class="grade-text" x="585" y="279" text-anchor="middle" textLength="176" lengthAdjust="spacingAndGlyphs">MGO300</text>

  <!-- Brand -->
  <text class="brand-name brand-name-shadow" x="597" y="375" text-anchor="middle" textLength="692" lengthAdjust="spacingAndGlyphs">TOROWAI DOWNS</text>
  <text class="brand-name" x="595" y="373" text-anchor="middle" textLength="692" lengthAdjust="spacingAndGlyphs">TOROWAI DOWNS</text>

  <!-- Pattern band -->
  <line class="band-rule" x1="120" y1="426" x2="1079" y2="426"/>
  <line class="band-rule" x1="120" y1="455" x2="1079" y2="455"/>
  <rect class="pattern-band" x="120" y="430" width="959" height="21" role="img" aria-label="Stylised Maori-inspired triangle pattern band"/>

  <!-- Product badge -->
  <path class="product-badge" d="M 398 393 Q 597 400 796 393 Q 808 393 808 405 L 808 473 Q 808 485 796 485 Q 597 478 398 485 Q 386 485 386 473 L 386 405 Q 386 393 398 393 Z"/>
  <path class="product-flourish" d="M 400 405 Q 597 412 794 405"/>
  <path class="product-flourish" d="M 400 473 Q 597 466 794 473"/>
  <text class="product-text" x="597" y="453" text-anchor="middle" textLength="356" lengthAdjust="spacingAndGlyphs">MANUKA HONEY</text>

  <!-- Net weight -->
  <text class="net-weight" transform="translate(1048 412) rotate(-90)">℮ 250g</text>
</svg>
</body>
</html>
```